Kitchen manufaturer business card/logo design

I am a small kitchen manufacturing company that makes and installs all sorts of cabinetry.

The colours im looking to incorporate in the card are light/baby blue, white and black.

Incorporate 5 stars to show quality workmanship and product.

Looking for a modern classy design.
Updates

Hey guys, New idea. The logo should be made using HK in the most modern way possible as well as the full company name below it. Thanks.

Target Market(s)

Anyone with a home thats looking for a new cabinetry of any sort.

Industry/Entity Type

Business

Contact Information for Business Card

Harbor Kitchens
Ted Lowther
PH 0491 358 902
Email- harborkitchens@mailvane.example
ABN- 83 507 962 318
-Kitchens
-Vanities
-Laundries
-Media Units
-Studies
-Wardrobes
-3D Computer Designs

Requirements
Must have

• The front of the card must only have the company name.
The different types of cabinetry I do must be on the back of the card in point form but instead of using points use stars.
Nice to have
• Just think classy and quality

```html
<!DOCTYPE html>
<html lang="en">
<head>
<meta charset="utf-8">
<title>Harbor Kitchens — Business Card</title>
<link rel="stylesheet" href="https://fonts.googleapis.com/css2?family=Cinzel:wght@600&family=Lato:wght@400;700&display=swap">
<style>
  :root {
    --ink: #000000;
    --paper: #ffffff;
    --brand-blue: #2f68b8;
    --backdrop: #e6e6e6;
    --text-light: #ffffff;
  }
  * { box-sizing: border-box; margin: 0; padding: 0; }
  html, body {
    width: 1200px; height: 1000px; overflow: hidden;
    background: var(--backdrop);
  }
  .canvas {
    width: 1200px; height: 1000px;
    display: flex; justify-content: center; align-items: center; gap: 80px;
  }
  .card {
    width: 420px; height: 735px; position: relative; overflow: hidden;
    box-shadow: 0 6px 18px rgba(0,0,0,0.25);
  }
  /* Front */
  .card--front {
    background: var(--ink);
    display: flex; justify-content: center; align-items: center;
  }
  .wordmark {
    display: flex; align-items: center; gap: 12px;
    font-family: "Cinzel", serif; font-weight: 600;
    letter-spacing: 1px;
  }
  .wordmark__square { width: 14px; height: 14px; background: var(--brand-blue); flex: none; }
  .wordmark__name { font-size: 30px; }
  .card--front .wordmark__name { color: var(--text-light); }
  /* Back */
  .card--back { background: var(--ink); }
  .back__top {
    height: 290px; background: var(--paper);
    display: flex; justify-content: center; align-items: center;
  }
  .card--back .wordmark__name { color: var(--ink); font-size: 28px; }
  .services {
    height: 110px; background: var(--brand-blue);
    display: flex; flex-direction: column; justify-content: center; align-items: center;
    font-family: "Lato", sans-serif; font-weight: 700; font-size: 18px; line-height: 1.2;
    color: var(--text-light); text-align: center;
  }
  .contact { padding: 60px 36px 0; }
  .contact__name {
    font-family: "Cinzel", serif; font-weight: 600; font-size: 34px;
    color: var(--brand-blue); letter-spacing: 2px; text-align: center;
    margin-bottom: 70px;
  }
  .contact__list { list-style: none; font-family: "Lato", sans-serif; font-size: 18px; color: var(--text-light); }
  .contact__list li { margin-bottom: 8px; white-space: nowrap; }
  .contact__label { color: var(--brand-blue); font-weight: 700; }
</style>
</head>
<body>
<main class="canvas">
  <section class="card card--front" aria-label="Card front">
    <div class="wordmark">
      <span class="wordmark__square"></span>
      <span class="wordmark__name">Harbor Kitchens</span>
    </div>
  </section>

  <section class="card card--back" aria-label="Card back">
    <div class="back__top">
      <div class="wordmark">
        <span class="wordmark__square"></span>
        <span class="wordmark__name">Harbor Kitchens</span>
      </div>
    </div>
    <div class="services">
      <p>Kitchens, Vanities, Laundries,</p>
      <p>Media Units, Studies, Wardrobes,</p>
      <p>3D Computer Designs</p>
    </div>
    <div class="contact">
      <h1 class="contact__name">TED LOWTHER</h1>
      <ul class="contact__list">
        <li><span class="contact__label">P:</span> 0491 358 902</li>
        <li><span class="contact__label">E:</span> harborkitchens@mailvane.example</li>
        <li><span class="contact__label">ABN:</span> 83 507 962 318</li>
      </ul>
    </div>
  </section>
</main>
</body>
</html>
```